Travel Company Itinerary and Travel Packet

I run a travel company (agency) that organizes trips (any length i.e. day, week, month, or longer) to countries (Israel, Italy, Greece, etc). Regardless of the destination, we want to provide appealing, professional, and clean materials. We are a firm believer that our product is not just the trip but in everything we do...from our communication to our written/printed materials and online presence. Today we are specifically looking for a template that we can use to share one's trip/itinerary. Ideally what you would create would be a template we could populate with specific information for the client about the day-to-day of their trip, who we are, the hotels they are staying in, the highlights, what to pack, and where to eat, etc. To be more specific, this template should consist of the following:
1. Title Page (including contact info...however this could go where you see fit)
2. About Us (blurb about us at the company),
3. A highlights page of the trip and services included - this could be used as standalone marketing material for our clients to promote trips. (look at the Italy example)
4. A timeline of the process
5. A summary of the trip, bullet point/all one 1 page
6. A day-by-day itinerary page of what they are doing, and where they are staying (each day on its own page - should be the same template repeated for each day.
7. Recommended Hotels to choose from
8. Recommended Restaurants to eat at
9. A pricing page (per person, per group, itemized down to each experience.
10. A packing List
11. A letterhead that could be used for a cover letter
12. Each page should use pictures...a template where one could insert photos per page based on where the trip is going as well as stock imaging that brings the document to life for the reader. (see examples in uploaded files).

We've attached a few that we've seen in the industry that appeals to us and our tastes, but the template we are looking for is even more eye-popping, user-friendly, and communicates a high level of service just by seeing the document. It communicates our brand. Each attached example has elements we like and don't like and will give you. a good picture (we hope), but you'll notice the list we gave you provides a more robust end product...in other words we want more than these examples as we see great potential in including each layer of information with the ability to pick and choose what to include (from all of it to just the highlights page).

Link to Brand Assets- https://files.plovanexa.net/share/folders/8Kd24mTqZrw91XbLcVn3pYe60hJ?mode=view
Updates

We need a few days to review the designs and had a few requests for an extension if possible. I've also uploaded sample itineraries for Israel as requested by a few designers. Much appreciated

Target Market(s)

Any client of ours traveling - school, groups, families, big spenders etc

Industry/Entity Type

Travel Industry

Requirements
Must have
• See above list - if clarification is needed, I'm happy to give.

```html
<!DOCTYPE html>
<html lang="en">
<head>
<meta charset="utf-8">
<title>Norvane – Itinerary Template Pages</title>
<link href="https://fonts.googleapis.com/css2?family=Montserrat:ital,wght@0,400;0,500;0,600;0,700;0,800;1,700;1,800&display=swap" rel="stylesheet">
<style>
:root{
  --backdrop:#7f9db5;
  --ink:#1f2833;
  --navy:#1d3750;
  --deep:#14202c;
  --orange:#d9884a;
  --yellow:#e6dd7a;
  --photo:#bfbfbf;
  --paper:#ffffff;
  --text:#2a2f36;
}
*{margin:0;padding:0;box-sizing:border-box}
html,body{width:1200px;height:1200px;overflow:hidden}
body{background:var(--backdrop);font-family:"Montserrat",sans-serif;color:var(--text);position:relative}
.page{position:absolute;width:305px;height:431px;background:var(--paper);overflow:hidden;box-shadow:0 2px 6px rgba(0,0,0,.25)}
.page--dark{background:var(--ink)}
.abs{position:absolute}
.wordmark{position:absolute;left:0;right:0;text-align:center;font-weight:800;color:var(--ink);font-size:36px;letter-spacing:-.5px}
.cover-title{position:absolute;left:0;right:0;text-align:center;line-height:1}
.cover-title .l1{font-weight:800;font-size:23px;color:var(--ink);display:block}
.cover-title .l2{font-weight:800;font-size:32px;color:var(--ink);display:block;margin-top:1px}
.cover-title .l3{font-weight:500;font-size:17px;color:var(--navy);display:block;margin-top:3px}
.cover-title .l4{font-weight:700;font-size:24px;color:var(--orange);display:block;margin-top:7px}
.cover-title--dark .l1,.cover-title--dark .l2{color:#fff;font-style:italic}
.cover-title--dark .l3{color:var(--yellow);font-size:18px;border-top:1px solid #2e3c4c;border-bottom:1px solid #2e3c4c;padding:6px 0;margin:6px 26px 0}
.cover-title--dark .l4{color:#fff;font-size:24px;margin-top:9px}
.cover-title--dark .l4 span{color:var(--orange)}
.band{position:absolute;left:0;top:23px;width:305px;height:32px}
.band-title{position:absolute;right:24px;top:31px;color:#fff;font-weight:700;font-size:14px;line-height:16px}
.toc{position:absolute;left:36px;top:132px;width:224px;list-style:none}
.toc li{display:flex;justify-content:space-between;font-size:5px;color:var(--text);height:19.5px;padding-top:5px;border-bottom:.8px solid var(--orange)}
.footer{position:absolute;left:0;top:398px;width:305px;height:16px}
.footer-url{position:absolute;left:24px;top:402px;font-size:5px;letter-spacing:1.3px;color:#dfe5eb}
.footer-mark{position:absolute;left:218px;top:401px;font-weight:800;font-size:9px;color:var(--navy)}
.footer-num{position:absolute;left:285px;top:401px;width:20px;text-align:center;font-size:6px;font-weight:700;color:#fff;line-height:10px}
.photo{position:absolute;background:var(--photo)}
.day-bar{position:absolute;background:var(--navy);color:var(--yellow);font-weight:700;font-size:7px;padding:0 5px;line-height:13px;height:13px}
.body-text{position:absolute;font-size:5.6px;line-height:1.5;color:var(--text);text-align:justify}
.body-text p{margin-bottom:7px}
.accent{color:var(--orange);font-weight:600}
.bullets{position:absolute;list-style:none;font-size:5.6px;line-height:1.5;color:var(--text)}
.bullets li{position:relative;padding-left:8px;text-align:justify}
.bullets li::before{content:"";position:absolute;left:1px;top:2.4px;width:3px;height:3px;border-radius:50%;background:var(--orange)}
.overnight{position:absolute;font-size:5.8px;color:var(--text)}
.contact-head{position:absolute;left:37px;top:321px;color:var(--orange);font-weight:800;font-size:8.5px}
.contact-list{position:absolute;left:37px;top:343px;list-style:none;font-size:6px;color:#fff;line-height:9px}
.contact-list li{display:flex;gap:4px;align-items:flex-start}
.contact-list svg{flex:none;margin-top:1px}
.back-mark{position:absolute;left:205px;top:352px;font-weight:800;font-size:16px;color:#fff}
</style>
</head>
<body>

<!-- Cover, light -->
<section class="page" style="left:104px;top:147px">
  <div class="wordmark" style="top:62px">Norvane</div>
  <h1 class="cover-title" style="top:237px">
    <span class="l1">CONGREGATION</span>
    <span class="l2">ITINERARY</span>
    <span class="l3">FAMILY ISRAEL TOUR</span>
    <span class="l4">JUNE 2022</span>
  </h1>
  <svg class="abs" style="left:0;top:0" width="305" height="431" viewBox="0 0 305 431">
    <polygon points="0,431 305,366 305,431" fill="var(--yellow)"/>
    <polygon points="38,431 305,377 305,431" fill="var(--orange)"/>
    <polygon points="108,431 305,390 305,431" fill="var(--navy)"/>
    <polygon points="220,431 305,412 305,431" fill="var(--ink)"/>
  </svg>
</section>

<!-- Cover, dark -->
<section class="page" style="left:450px;top:147px">
  <div class="wordmark" style="top:64px">Norvane</div>
  <svg class="abs" style="left:0;top:0" width="305" height="431" viewBox="0 0 305 431">
    <polygon points="0,226 305,165 305,431 0,431" fill="var(--yellow)"/>
    <polygon points="0,238 305,177 305,431 0,431" fill="var(--orange)"/>
    <polygon points="0,251 305,190 305,431 0,431" fill="var(--navy)"/>
    <polygon points="0,264 305,203 305,431 0,431" fill="var(--ink)"/>
  </svg>
  <h1 class="cover-title cover-title--dark" style="top:272px">
    <span class="l1">CONGREGATION</span>
    <span class="l2">ITINERARY</span>
    <span class="l3">FAMILY ISRAEL TOUR</span>
    <span class="l4">JUNE <span>2022</span></span>
  </h1>
</section>

<!-- Table of contents -->
<section class="page" style="left:796px;top:147px">
  <svg class="band" viewBox="0 0 305 32">
    <polygon points="0,0 50,0 66,32 0,32" fill="var(--navy)"/>
    <polygon points="24,0 34,0 50,32 40,32" fill="var(--deep)"/>
    <polygon points="50,0 62,0 78,32 66,32" fill="var(--yellow)"/>
    <polygon points="62,0 305,0 305,32 78,32" fill="var(--orange)"/>
  </svg>
  <h2 class="band-title">TABLE OF CONTENTS</h2>
  <ol class="toc">
    <li><span>01. DIAM NONUMMY NIBH EUISMOD TINCIDUNT</span><span>01</span></li>
    <li><span>02. UT LAOREET DOLORE MAGNA ALIQUAM ERAT VOLUTPAT.</span><span>03</span></li>
    <li><span>03. UT WISI ENIM AD MINIM VENIAM, QUIS NOSTRUD EXERCI</span><span>04</span></li>
    <li><span>04. TATION ULLAMCORPER SUSCIPIT LOBORTIS NISL</span><span>05</span></li>
    <li><span>05. UT ALIQUIP EX EA COMMODO CONSEQUAT.</span><span>06</span></li>
    <li><span>06. DUIS AUTEM VEL EUM IRIURE DOLOR IN HENDRERIT</span><span>07</span></li>
    <li><span>07. IN VULPUTATE VELIT ESSE MOLESTIE CONSEQUAT,</span><span>08</span></li>
    <li><span>08. VEL ILLUM DOLORE EU FEUGIAT NULLA FACILISIS AT</span><span>09</span></li>
    <li><span>09. VERO EROS ET ACCUMSAN ET IUSTO ODIO DIGNISSIM</span><span>09</span></li>
    <li><span>10. QUI BLANDIT PRAESENT LUPTATUM ZZRIL DELENIT</span><span>09</span></li>
  </ol>
  <svg class="footer" viewBox="0 0 305 16">
    <polygon points="0,0 206,0 214,16 0,16" fill="var(--ink)"/>
    <polygon points="209,0 212,0 220,16 217,16" fill="var(--ink)"/>
    <polygon points="274,0 278,0 286,16 282,16" fill="var(--yellow)"/>
    <polygon points="280,0 305,0 305,16 288,16" fill="var(--orange)"/>
  </svg>
  <span class="footer-url">www.norvane.com</span>
  <span class="footer-mark">Norvane</span>
  <span class="footer-num">1</span>
</section>

<!-- About us / Day 0–1 -->
<section class="page" style="left:104px;top:624px">
  <svg class="band" viewBox="0 0 305 32">
    <polygon points="0,0 50,0 66,32 0,32" fill="var(--navy)"/>
    <polygon points="24,0 34,0 50,32 40,32" fill="var(--deep)"/>
    <polygon points="50,0 62,0 78,32 66,32" fill="var(--yellow)"/>
    <polygon points="62,0 305,0 305,32 78,32" fill="var(--orange)"/>
  </svg>
  <h2 class="band-title">ABOUT US</h2>
  <div class="photo" role="img" aria-label="Photo of the destination" style="left:23px;top:83px;width:115px;height:148px"></div>
  <div class="day-bar" style="left:151px;top:83px;width:130px">DAY 0: – ARRIVAL IN ISRAEL</div>
  <div class="body-text" style="left:151px;top:100px;width:130px">
    <p><span class="accent">Welcome to Israel!</span> – Arrive on your own to the Holy Land. Feel free to rest up before the trip or explore the city of Tel Aviv on your own. Make sure to save something for the trip though!</p>
    <p><span class="accent">Overnight:</span> Early arrivals can stay at the Seaside Court Hotel, Tel Aviv or Dune Crest Hotel, Sde Boker – Not included in the price of the tour, prices to be advised individually</p>
    <p style="text-align:left"><span class="accent">Flight options:</span><br><b style="font-weight:500;color:var(--ink)">SKYLINE 5:20PM<br>Meridian 9:20 AM<br>Northway Air 10:15 AM</b></p>
  </div>
  <div class="day-bar" style="left:23px;top:248px;width:258px">DAY 1:– ON THE WAY SOUTH</div>
  <ul class="bullets" style="left:23px;top:268px;width:258px">
    <li>Breakfast at the hotel</li>
    <li>The Garden Trail - We'll walk through “The Garden Trail”, Shvil Hagan, a working farm and interactive museum designed to teach visitors what it takes to farm and grow crops in the desert (a window to the Israeli world famous Hi-tech agriculture).</li>
    <li>Lunch at the Garden Trail</li>
    <li>Sandboarding – Slide down the stunning Negev dunes, where anyone can be a surfer.</li>
    <li>Check in to hotel and get ready for shabbat</li>
    <li>Shabbat Service at the hotel and Lighting Chanukah Candles</li>
    <li>Shabbat Dinner at the hotel</li>
  </ul>
  <p class="overnight" style="left:32px;top:367px"><span class="accent">Overnight:</span> Dune Crest Hotel, Sde Boker</p>
  <svg class="footer" viewBox="0 0 305 16">
    <polygon points="0,0 206,0 214,16 0,16" fill="var(--ink)"/>
    <polygon points="209,0 212,0 220,16 217,16" fill="var(--ink)"/>
    <polygon points="274,0 278,0 286,16 282,16" fill="var(--yellow)"/>
    <polygon points="280,0 305,0 305,16 288,16" fill="var(--orange)"/>
  </svg>
  <span class="footer-url">www.norvane.com</span>
  <span class="footer-mark">Norvane</span>
  <span class="footer-num">1</span>
</section>

<!-- Why us / Day 2 -->
<section class="page" style="left:450px;top:624px">
  <svg class="band" viewBox="0 0 305 32">
    <polygon points="0,0 50,0 66,32 0,32" fill="var(--navy)"/>
    <polygon points="24,0 34,0 50,32 40,32" fill="var(--deep)"/>
    <polygon points="50,0 62,0 78,32 66,32" fill="var(--yellow)"/>
    <polygon points="62,0 305,0 305,32 78,32" fill="var(--orange)"/>
  </svg>
  <h2 class="band-title">WHY US</h2>
  <div class="photo" role="img" aria-label="Wide photo of the desert landscape" style="left:24px;top:81px;width:258px;height:114px"></div>
  <div class="day-bar" style="left:24px;top:203px;width:258px">DAY 2:– SHABBAT IN THE DESERT</div>
  <ul class="bullets" style="left:24px;top:224px;width:258px">
    <li>Breakfast at the hotel</li>
    <li>Special Shabbat Service –in the desert!</li>
    <li>Lunch at the hotel</li>
    <li><b style="font-weight:700;color:var(--ink)">Ein Avdat</b> – A shaded canyon in the Negev Desert of Israel. Archaeological evidence shows that Ein Avdat was inhabited by Nabateans and Catholic monks. Numerous springs at the southern opening of the canyon empty into deep pools in a series of waterfalls. The water emerges from the rock layers with salt-tolerant plants like Poplar trees and Atriplexes growing nearby.</li>
    <li><b style="font-weight:700;color:var(--ink)">Camel Ride – at Khan Midbar Camp (each bus separately during the day)<br>Founders' Tomb</b> - The graves of Aaron and Miriam Halev overlook a breathtaking view of the Tsin canyon and the Avdat highlands in the heart of the Negev. The path from the parking lot to the tranquil grave site goes through a garden of carefully nurtured local flora that can thrive in the arid climate and saline conditions of the local soil.</li>
    <li>Bedouin “Hafla” at Khan Midbar Camp – Including a delicious Bedouin meal &amp; many surprises!</li>
  </ul>
  <p class="overnight" style="left:32px;top:370px"><span class="accent">Overnight:</span> Dune Crest Hotel, Sde Boker</p>
  <svg class="footer" viewBox="0 0 305 16">
    <polygon points="0,0 206,0 214,16 0,16" fill="var(--ink)"/>
    <polygon points="209,0 212,0 220,16 217,16" fill="var(--ink)"/>
    <polygon points="274,0 278,0 286,16 282,16" fill="var(--yellow)"/>
    <polygon points="280,0 305,0 305,16 288,16" fill="var(--orange)"/>
  </svg>
  <span class="footer-url">www.norvane.com</span>
  <span class="footer-mark">Norvane</span>
  <span class="footer-num">1</span>
</section>

<!-- Back cover -->
<section class="page page--dark" style="left:796px;top:624px">
  <h3 class="contact-head">CONTACT US</h3>
  <ul class="contact-list">
    <li><svg width="5" height="6" viewBox="0 0 10 12"><path d="M5 0a4 4 0 0 0-4 4c0 3 4 8 4 8s4-5 4-8a4 4 0 0 0-4-4zm0 5.5a1.5 1.5 0 1 1 0-3 1.5 1.5 0 0 1 0 3z" fill="var(--yellow)"/></svg><span>214 Harbor Street<br>Portland, Oregon 97201</span></li>
    <li style="margin-top:4px"><svg width="5" height="5" viewBox="0 0 10 10"><path d="M2 0l2 2-1 2c1 1.5 2 2.5 3 3l2-1 2 2-1.5 2C4 10 0 6 0 1.5z" fill="var(--yellow)"/></svg><span>555-014-2280</span></li>
    <li><svg width="5" height="5" viewBox="0 0 10 8"><rect width="10" height="8" fill="var(--yellow)"/><path d="M0 0l5 4 5-4" stroke="var(--ink)" fill="none"/></svg><span>info@norvane.com</span></li>
    <li><svg width="5" height="5" viewBox="0 0 10 10"><circle cx="5" cy="5" r="5" fill="var(--yellow)"/></svg><span>norvane.com</span></li>
  </ul>
  <span class="back-mark">Norvane</span>
</section>

</body>
</html>
```